PPT Template for an investment fund to use in their pitchbooks

Our firm is an international investment fund and are seeking a PPT template to use in our pitch book (and subsequent PPTs). We would need a template for a title slide and then subsequent text/info slides. A clean & uncluttered feel is preferred as well as no watermark on slides. Please see our logo attached. The logo color code is #19478d. Font is Gotham-Medium.

Target Market(s)

Sophisticated investors

Industry/Entity Type

Finance

Colors
ffffff
0356a4

```html
<!DOCTYPE html>
<html lang="en">
<head>
<meta charset="utf-8">
<title>Halvern Capital – Pitchbook Template</title>
<link href="https://fonts.googleapis.com/css2?family=Montserrat:ital,wght@0,500;0,600;0,700;0,800;1,600;1,700&display=swap" rel="stylesheet">
<style>
  :root{
    --page:#e3e3e3;
    --blue:#1f4ea3;
    --blue-bright:#3b6fd4;
    --blue-light:#8fb0ec;
    --blue-pale:#c9d6f2;
    --ink:#16191f;
    --charcoal:#323844;
    --grey:#5f646d;
    --white:#ffffff;
    --photo-dark:#2b2f37;
    --photo-light:#9a9fa8;
  }
  *{margin:0;padding:0;box-sizing:border-box}
  html,body{width:1200px;height:560px;overflow:hidden;background:var(--page)}
  body{font-family:"Montserrat",sans-serif;position:relative}
  .slide{position:absolute;width:284px;height:159px;overflow:hidden;display:block}
  .slide svg{width:284px;height:159px;display:block}
  .r1{top:29px}.r2{top:200px}.r3{top:369px}
  .c1{left:18px}.c2{left:311px}.c3{left:604px}.c4{left:898px}

  text{font-family:"Montserrat",sans-serif}
  .title{font-size:21px;font-weight:700}
  .title-sm{font-size:17px;font-weight:700}
  .lead{font-size:13px;font-weight:700;font-style:italic}
  .body{font-size:9.2px;font-weight:500}
  .body-b{font-size:9.2px;font-weight:700}
  .tiny{font-size:4.2px;font-weight:500}
  .tag{font-size:7.5px;font-weight:600}
  .label{font-size:8.5px;font-weight:700}
  .fill-white{fill:var(--white)}
  .fill-blue{fill:var(--blue)}
  .fill-bright{fill:var(--blue-bright)}
  .fill-light{fill:var(--blue-light)}
  .fill-ink{fill:var(--ink)}
  .fill-grey{fill:var(--grey)}
  .stripe{fill:none;stroke-linecap:round}
</style>
</head>
<body>

<!-- Title slide -->
<div class="slide r1 c1">
<svg viewBox="0 0 610 342">
  <defs>
    <linearGradient id="skyline" x1="0" y1="0" x2="1" y2="1">
      <stop offset="0" stop-color="#ffffff"/><stop offset="1" stop-color="#e6e7ea"/>
    </linearGradient>
    <linearGradient id="photo" x1="0" y1="0" x2="1" y2="1">
      <stop offset="0" stop-color="#2b2f37"/><stop offset="1" stop-color="#9a9fa8"/>
    </linearGradient>
  </defs>
  <rect width="610" height="342" fill="url(#skyline)" role="img" aria-label="Faint photograph of office towers"/>
  <path class="stripe" d="M70 342 L217 118 L360 342" stroke="#d7d9dd" stroke-width="16"/>
  <path class="stripe" d="M145 290 L215 180" stroke="#b9cbef" stroke-width="12"/>
  <path d="M110 342 L217 178 L330 342 Z" fill="#dfe1e5"/>
  <rect x="37" y="56" width="12" height="12" fill="var(--blue)"/>
  <text x="55" y="67" class="label fill-blue">HALVERN CAPITAL</text>
  <text x="230" y="277" class="body-b" fill="#f4f5f7" text-anchor="middle" style="font-size:14px">
    <tspan x="230">Your</tspan><tspan x="230" dy="18">Headline</tspan><tspan x="230" dy="18">Here</tspan>
  </text>
  <text x="386" y="178" class="lead fill-blue" style="font-style:normal">
    <tspan x="386">Morbi cursus suscipit</tspan><tspan x="386" dy="16">lectus vitae ornare.</tspan>
  </text>
  <text x="386" y="217" class="body fill-ink">
    <tspan x="386">Curabitur dignissim, tellus nec euismod</tspan>
    <tspan x="386" dy="12">mollis dapibus, ex sapien lacinia ligula,</tspan>
    <tspan x="386" dy="12">nec ullamcorper arcu lorem vel lorem.</tspan>
    <tspan x="386" dy="12">Sed id ante at quam euismod commodo</tspan>
    <tspan x="386" dy="12">quis vitae nisl ullamcorper arcu lorem.</tspan>
  </text>
  <text x="386" y="300" class="body-b fill-blue">Etiam quam sapien, faucibus vitae.</text>
</svg>
</div>

<!-- Intro text slide -->
<div class="slide r1 c2">
<svg viewBox="0 0 610 342">
  <rect width="610" height="342" fill="var(--blue)"/>
  <path class="stripe" d="M10 20 L185 295" stroke="var(--blue-bright)" stroke-width="14"/>
  <polygon points="97,129 307,129 212,294" fill="url(#photo)" role="img" aria-label="Photograph of a trading screen"/>
  <path class="stripe" d="M285 110 L235 290" stroke="var(--white)" stroke-width="12"/>
  <text x="98" y="80" class="lead fill-white">
    <tspan x="98">Morbi cursus suscipit</tspan><tspan x="98" dy="16">lectus vitae ornare.</tspan>
  </text>
  <text x="336" y="88" class="title fill-white">SUSPENDISSE</text>
  <text x="336" y="117" class="title fill-light">SAPIEN TURPIS.</text>
  <text x="336" y="148" class="body fill-white">
    <tspan x="336">Curabitur dignissim, tellus nec euismod</tspan>
    <tspan x="336" dy="12">mollis dapibus, ex sapien lacinia ligula,</tspan>
    <tspan x="336" dy="12">nec ullamcorper arcu lorem vel lorem.</tspan>
    <tspan x="336" dy="12">Sed id ante at quam euismod commodo</tspan>
    <tspan x="336" dy="12">quis vitae nisl ullamcorper arcu lorem.</tspan>
    <tspan x="336" dy="22">Cras eget est faucibus, dapibus mi in,</tspan>
    <tspan x="336" dy="12">tempor nulla. Aliquam et lobortis ipsum.</tspan>
    <tspan x="336" dy="12">Cras urna velit, dictum posuere dolor at,</tspan>
    <tspan x="336" dy="12">facilisis maximus nunc.</tspan>
  </text>
  <text x="336" y="278" class="body-b fill-light">
    <tspan x="336">Duis mollis ante imperdiet volutpat dapibus.</tspan>
    <tspan x="336" dy="12">Morbi molestie odio vel ultricies aliquet.</tspan>
  </text>
</svg>
</div>

<!-- Percentage slide -->
<div class="slide r1 c3">
<svg viewBox="0 0 610 342">
  <rect width="610" height="342" fill="var(--white)"/>
  <polygon points="520,0 610,0 610,150" fill="url(#photo)" role="img" aria-label="Photograph of market data figures"/>
  <path class="stripe" d="M530 8 L610 80" stroke="var(--charcoal)" stroke-width="14"/>
  <path class="stripe" d="M515 70 L610 150" stroke="var(--blue-bright)" stroke-width="12"/>
  <text x="298" y="86" class="title fill-blue" text-anchor="middle">PELLENT ESQUE EST MAGNA.</text>
  <g>
    <polygon points="100,180 128,186 104,206" fill="var(--blue-light)"/>
    <circle cx="115" cy="147" r="43" fill="var(--charcoal)"/>
    <circle cx="115" cy="147" r="33" fill="none" stroke="var(--blue-light)" stroke-width="4" stroke-dasharray="151 207" transform="rotate(-90 115 147)"/>
    <text x="115" y="153" class="title-sm fill-light" text-anchor="middle" style="font-size:15px">73 <tspan style="font-size:7px">%</tspan></text>

    <polygon points="215,180 243,186 219,206" fill="var(--blue-light)"/>
    <circle cx="230" cy="147" r="43" fill="var(--charcoal)"/>
    <circle cx="230" cy="147" r="33" fill="none" stroke="var(--blue-light)" stroke-width="4" stroke-dasharray="174 207" transform="rotate(-90 230 147)"/>
    <text x="230" y="153" class="title-sm fill-light" text-anchor="middle" style="font-size:15px">84 <tspan style="font-size:7px">%</tspan></text>

    <polygon points="329,180 357,186 333,206" fill="var(--blue-light)"/>
    <circle cx="344" cy="147" r="43" fill="var(--charcoal)"/>
    <circle cx="344" cy="147" r="33" fill="none" stroke="var(--blue-light)" stroke-width="4" stroke-dasharray="139 207" transform="rotate(-90 344 147)"/>
    <text x="344" y="153" class="title-sm fill-light" text-anchor="middle" style="font-size:15px">67 <tspan style="font-size:7px">%</tspan></text>

    <polygon points="445,180 473,186 449,206" fill="var(--blue-light)"/>
    <circle cx="460" cy="147" r="43" fill="var(--charcoal)"/>
    <circle cx="460" cy="147" r="33" fill="none" stroke="var(--blue-light)" stroke-width="4" stroke-dasharray="197 207" transform="rotate(-90 460 147)"/>
    <text x="460" y="153" class="title-sm fill-light" text-anchor="middle" style="font-size:15px">95 <tspan style="font-size:7px">%</tspan></text>
  </g>
  <g class="body fill-grey">
    <text x="65" y="234"><tspan class="body-b fill-blue">Curabitur digni</tspan><tspan x="65" dy="12">tellus nec euismod</tspan><tspan x="65" dy="12">mollis dapibus, ex</tspan><tspan x="65" dy="12">sapien lacinia ligula,</tspan><tspan x="65" dy="12">nec ullamcorper arcu</tspan><tspan x="65" dy="12">lorem vel lorem.</tspan></text>
    <text x="179" y="234"><tspan class="body-b fill-blue">Euismod mollis</tspan><tspan x="179" dy="12">bus, ex sapien lacinia</tspan><tspan x="179" dy="12">ligula, nec ullamcorper</tspan><tspan x="179" dy="12">arcu lorem vel lorem.</tspan><tspan x="179" dy="12">Sed id ante at quam</tspan><tspan x="179" dy="12">euismod commodo</tspan></text>
    <text x="300" y="234"><tspan class="body-b fill-blue">La cinia ligula</tspan><tspan x="300" dy="12">ullamcorper arcu</tspan><tspan x="300" dy="12">lorem vel lorem.</tspan><tspan x="300" dy="12">Sed id ante at quam</tspan><tspan x="300" dy="12">euismod commodo</tspan><tspan x="300" dy="12">quis vitae nisl ullam</tspan></text>
    <text x="417" y="234"><tspan class="body-b fill-blue">Sed id ante at</tspan><tspan x="417" dy="12">euismod commodo</tspan><tspan x="417" dy="12">quis vitae nisl ullam</tspan><tspan x="417" dy="12">corper arcu lorem.</tspan><tspan x="417" dy="12">Curabitur dignissim,</tspan><tspan x="417" dy="12">tellus nec euismod</tspan></text>
  </g>
</svg>
</div>

<!-- Timeline slide -->
<div class="slide r1 c4">
<svg viewBox="0 0 610 342">
  <rect width="610" height="342" fill="var(--blue)"/>
  <polygon points="70,342 150,230 200,342" fill="url(#photo)" role="img" aria-label="Photograph of a trading tablet"/>
  <path class="stripe" d="M50 342 L140 220" stroke="var(--blue-bright)" stroke-width="12"/>
  <path class="stripe" d="M150 225 L195 300" stroke="var(--white)" stroke-width="9"/>
  <text x="63" y="86" class="title fill-white">CURABITUR</text>
  <text x="63" y="115" class="title fill-light">TINCIDUNT</text>
  <text x="63" y="144" class="title fill-white">OSUERE.</text>
  <text x="63" y="167" class="body-b fill-light"><tspan x="63">Duis mollis ante imperdiet</tspan><tspan x="63" dy="12">Morbi molestie odio vel.</tspan></text>

  <line x1="393" y1="71" x2="393" y2="267" stroke="var(--white)" stroke-width="2"/>
  <g stroke="var(--white)" stroke-width="1.5">
    <line x1="327" y1="87" x2="435" y2="87"/>
    <line x1="327" y1="143" x2="435" y2="143"/>
    <line x1="327" y1="199" x2="435" y2="199"/>
    <line x1="327" y1="255" x2="435" y2="255"/>
  </g>
  <g class="tiny" fill="var(--blue)" text-anchor="middle" style="font-size:5px;font-weight:700">
    <circle cx="393" cy="71" r="9" fill="var(--white)"/><text x="393" y="73">2017</text>
    <circle cx="393" cy="105" r="9" fill="var(--white)"/><text x="393" y="107">2016</text>
    <circle cx="393" cy="138" r="9" fill="var(--white)"/><text x="393" y="140">2015</text>
    <circle cx="393" cy="172" r="9" fill="var(--white)"/><text x="393" y="174">2014</text>
    <circle cx="393" cy="206" r="9" fill="var(--white)"/><text x="393" y="208">2013</text>
    <circle cx="393" cy="267" r="9" fill="var(--white)"/><text x="393" y="269">Start</text>
  </g>
  <g>
    <rect x="253" y="67" width="74" height="40" fill="var(--white)"/>
    <rect x="253" y="123" width="74" height="40" fill="var(--white)"/>
    <rect x="253" y="179" width="74" height="40" fill="var(--white)"/>
    <rect x="253" y="235" width="74" height="40" fill="var(--white)"/>
    <rect x="435" y="67" width="100" height="40" fill="var(--white)"/>
    <rect x="435" y="123" width="100" height="40" fill="var(--white)"/>
    <rect x="435" y="179" width="100" height="40" fill="var(--white)"/>
    <rect x="435" y="235" width="100" height="40" fill="var(--white)"/>
    <g fill="var(--blue)">
      <polygon points="256,71 264,75 256,79"/><polygon points="256,127 264,131 256,135"/>
      <polygon points="256,183 264,187 256,191"/><polygon points="256,239 264,243 256,247"/>
      <polygon points="438,71 446,75 438,79"/><polygon points="438,127 446,131 438,135"/>
      <polygon points="438,183 446,187 438,191"/><polygon points="438,239 446,243 438,247"/>
    </g>
    <g class="tag fill-blue" style="font-size:7px">
      <text x="267" y="78">Nam vulputat</text><text x="267" y="134">Duis porttitor</text>
      <text x="267" y="190">Pellentesque</text><text x="267" y="246">Suspendisse</text>
      <text x="449" y="78">Pellentesque</text><text x="449" y="134">Suspendisse</text>
      <text x="449" y="190">Nam vulputat</text><text x="449" y="246">Duis porttitor</text>
    </g>
    <g class="tiny fill-grey">
      <text x="262" y="86"><tspan x="262">Donec laoreet commodo dictum.</tspan><tspan x="262" dy="5">Suspendisse vulputate, mauris in</tspan><tspan x="262" dy="5">ultrices pretium, nunc lectus.</tspan></text>
      <text x="262" y="142"><tspan x="262">Vestibulum pretium nisi sit amet.</tspan><tspan x="262" dy="5">Nam commodo leo a purus semper.</tspan><tspan x="262" dy="5">Sed consequat libero a arcu.</tspan></text>
      <text x="262" y="198"><tspan x="262">Suspendisse vulputate, mauris in</tspan><tspan x="262" dy="5">pretium, nunc pellentesque nisi.</tspan><tspan x="262" dy="5">tempus elit nunc lectus.</tspan></text>
      <text x="262" y="254"><tspan x="262">Curabitur suscipit tincidunt.</tspan><tspan x="262" dy="5">Nam commodo leo a purus semper.</tspan><tspan x="262" dy="5">eget scelerisque erat.</tspan></text>
      <text x="444" y="86"><tspan x="444">Suspendisse vulputate, mauris in ultri</tspan><tspan x="444" dy="5">pretium, nunc pellentesque nisi lectus</tspan><tspan x="444" dy="5">ultrices pretium, nunc lectus sodales.</tspan></text>
      <text x="444" y="142"><tspan x="444">Curabitur suscipit tincidunt hendrerit.</tspan><tspan x="444" dy="5">Nam commodo leo a purus semper,</tspan><tspan x="444" dy="5">eget scelerisque erat venenatis.</tspan></text>
      <text x="444" y="198"><tspan x="444">Donec laoreet commodo dictum.</tspan><tspan x="444" dy="5">Suspendisse vulputate, mauris in</tspan><tspan x="444" dy="5">ultrices pretium, nunc lectus sodales.</tspan></text>
      <text x="444" y="254"><tspan x="444">Vestibulum pretium nisi sit amet ligula</tspan><tspan x="444" dy="5">porta, non pellentesque metus sodales.</tspan><tspan x="444" dy="5">Sed consequat libero a arcu convallis.</tspan></text>
    </g>
  </g>
</svg>
</div>

<!-- Table slide -->
<div class="slide r2 c1">
<svg viewBox="0 0 610 342">
  <rect width="610" height="342" fill="var(--white)"/>
  <polygon points="402,0 610,0 610,342 252,342" fill="var(--blue)"/>
  <path class="stripe" d="M410 -5 L495 140" stroke="var(--blue-bright)" stroke-width="12"/>
  <path class="stripe" d="M455 10 L540 145" stroke="var(--blue-light)" stroke-width="10"/>
  <path class="stripe" d="M590 -5 L545 65" stroke="var(--white)" stroke-width="12"/>
  <text x="80" y="78" class="lead fill-ink"><tspan x="80">Morbi cursus suscipit</tspan><tspan x="80" dy="16">lectus vitae ornare.</tspan></text>
  <g>
    <rect x="77" y="115" width="68" height="23" fill="var(--blue)"/>
    <rect x="147" y="115" width="68" height="23" fill="var(--blue)"/>
    <rect x="217" y="115" width="68" height="23" fill="var(--blue)"/>
    <rect x="287" y="115" width="68" height="23" fill="var(--blue)"/>
    <g class="tag fill-white" text-anchor="middle"><text x="111" y="130">Nam vulput</text><text x="181" y="130">Duis porttitor</text><text x="251" y="130">Pellentesque</text><text x="321" y="130">Suspendisse</text></g>
  </g>
  <g fill="#e9ebef">
    <rect x="77" y="150" width="278" height="28"/><rect x="77" y="182" width="278" height="28"/>
    <rect x="77" y="214" width="278" height="28"/><rect x="77" y="246" width="278" height="28"/>
  </g>
  <g stroke="var(--charcoal)" stroke-width="2"><line x1="146" y1="150" x2="146" y2="274"/><line x1="216" y1="150" x2="216" y2="274"/><line x1="286" y1="150" x2="286" y2="274"/><line x1="356" y1="150" x2="356" y2="274"/></g>
  <g fill="var(--charcoal)">
    <rect x="40" y="150" width="36" height="28"/><rect x="40" y="182" width="36" height="28"/>
    <rect x="40" y="214" width="36" height="28"/><rect x="40" y="246" width="36" height="28"/>
  </g>
  <g class="label fill-white" text-anchor="middle" style="font-size:10px"><text x="58" y="168">01</text><text x="58" y="200">02</text><text x="58" y="232">03</text><text x="58" y="264">04</text></g>
  <g class="tiny fill-grey">
    <text x="82" y="160"><tspan x="82">Aenean finibus, lorem vitae</tspan><tspan x="82" dy="5">aliquet volutpat, nibh</tspan><tspan x="82" dy="5">ligula dictum elit.</tspan></text>
    <text x="152" y="160"><tspan x="152">Sed ornare urna eu libero</tspan><tspan x="152" dy="5">auctor, a euismod magna</tspan><tspan x="152" dy="5">semper donec.</tspan></text>
    <text x="249" y="166">–</text>
    <text x="292" y="160"><tspan x="292">Aliquam a justo nisi. Cras</tspan><tspan x="292" dy="5">ultricies nisi quis odio.</tspan></text>
    <text x="82" y="192"><tspan x="82">Aliquam a justo nisi. Cras</tspan><tspan x="82" dy="5">ultricies nisi quis odio</tspan><tspan x="82" dy="5">blandit.</tspan></text>
    <text x="152" y="192"><tspan x="152">Aenean finibus, lorem vitae</tspan><tspan x="152" dy="5">aliquet volutpat, nibh</tspan><tspan x="152" dy="5">ligula dictum elit.</tspan></text>
    <text x="222" y="192"><tspan x="222">Sed ornare urna eu libero</tspan><tspan x="222" dy="5">auctor, a euismod magna</tspan><tspan x="222" dy="5">semper.</tspan></text>
    <text x="292" y="192"><tspan x="292">Aenean finibus, lorem vitae</tspan><tspan x="292" dy="5">aliquet volutpat, nibh</tspan><tspan x="292" dy="5">ligula dictum elit.</tspan></text>
    <text x="82" y="224"><tspan x="82">Sed ornare urna eu libero</tspan><tspan x="82" dy="5">auctor, a euismod magna</tspan><tspan x="82" dy="5">semper donec.</tspan></text>
    <text x="152" y="224"><tspan x="152">Aliquam a justo nisi. Cras</tspan><tspan x="152" dy="5">ultricies nisi quis odio</tspan><tspan x="152" dy="5">blandit.</tspan></text>
    <text x="249" y="230">–</text>
    <text x="292" y="224"><tspan x="292">Sed ornare urna eu libero</tspan><tspan x="292" dy="5">auctor, a euismod magna</tspan><tspan x="292" dy="5">semper donec.</tspan></text>
    <text x="109" y="262">–</text>
    <text x="152" y="256"><tspan x="152">Aenean finibus, lorem vitae</tspan><tspan x="152" dy="5">aliquet volutpat, nibh</tspan><tspan x="152" dy="5">ligula dictum elit.</tspan></text>
    <text x="222" y="256"><tspan x="222">Sed ornare urna eu libero</tspan><tspan x="222" dy="5">auctor, a euismod magna</tspan><tspan x="222" dy="5">semper.</tspan></text>
    <text x="319" y="262">–</text>
  </g>
  <text x="404" y="189" class="title fill-white">PORTTITOR</text>
  <text x="404" y="218" class="title fill-light">TURPIS SAPIEN</text>
  <text x="404" y="247" class="title fill-white">SUSPENDISSE</text>
  <text x="404" y="270" class="body-b fill-white"><tspan x="404">Duis mollis ante imperdiet</tspan><tspan x="404" dy="12">Morbi molestie odio vel.</tspan></text>
</svg>
</div>

<!-- Process slide -->
<div class="slide r2 c2">
<svg viewBox="0 0 610 342">
  <rect width="610" height="342" fill="var(--white)"/>
  <rect x="243" width="367" height="342" fill="var(--ink)"/>
  <path class="stripe" d="M455 -5 L500 70" stroke="var(--blue)" stroke-width="14"/>
  <path class="stripe" d="M485 -5 L530 70" stroke="var(--blue-bright)" stroke-width="12"/>
  <path class="stripe" d="M580 -5 L540 62" stroke="#d5d8de" stroke-width="12"/>
  <g fill="none" stroke="var(--blue-bright)" stroke-width="2.5">
    <path d="M60 108 Q45 118 70 120 L183 120"/>
    <path d="M190 149 Q205 159 180 161 L67 161"/>
    <path d="M60 190 Q45 200 70 202 L183 202"/>
    <path d="M190 231 Q205 241 180 243 L67 243"/>
  </g>
  <g fill="var(--blue-bright)">
    <polygon points="178,116 186,120 178,124"/><polygon points="72,157 64,161 72,165"/>
    <polygon points="178,198 186,202 178,206"/><polygon points="72,239 64,243 72,247"/>
  </g>
  <g>
    <circle cx="67" cy="93" r="15" fill="var(--charcoal)" stroke="var(--blue-bright)" stroke-width="2.5"/>
    <circle cx="183" cy="134" r="15" fill="var(--charcoal)" stroke="var(--blue-bright)" stroke-width="2.5"/>
    <circle cx="67" cy="175" r="15" fill="var(--charcoal)" stroke="var(--blue-bright)" stroke-width="2.5"/>
    <circle cx="183" cy="216" r="15" fill="var(--charcoal)" stroke="var(--blue-bright)" stroke-width="2.5"/>
    <circle cx="67" cy="257" r="15" fill="var(--charcoal)" stroke="var(--blue-bright)" stroke-width="2.5"/>
    <g class="label fill-white" text-anchor="middle" style="font-size:11px"><text x="67" y="97">01</text><text x="183" y="138">02</text><text x="67" y="179">03</text><text x="183" y="220">04</text><text x="67" y="261">05</text></g>
  </g>
  <g class="tiny fill-ink">
    <text x="88" y="86"><tspan x="88" style="font-weight:700;font-size:5px">Duis porttitor, orci sit amet</tspan><tspan x="88" dy="5">Phasellus bibendum consequat facilisis.</tspan><tspan x="88" dy="5">Vivamus non eros at enim bibendum</tspan><tspan x="88" dy="5">congue nisi. Nam pretium elementum.</tspan></text>
    <text x="60" y="127"><tspan x="60" style="font-weight:700;font-size:5px">Duis porttitor, orci sit amet</tspan><tspan x="60" dy="5">Phasellus bibendum consequat facilisis.</tspan><tspan x="60" dy="5">Vivamus non eros at enim bibendum</tspan><tspan x="60" dy="5">congue nisi. Nam pretium elementum.</tspan></text>
    <text x="88" y="168"><tspan x="88" style="font-weight:700;font-size:5px">Duis porttitor, orci sit amet</tspan><tspan x="88" dy="5">Phasellus bibendum consequat facilisis.</tspan><tspan x="88" dy="5">Vivamus non eros at enim bibendum</tspan><tspan x="88" dy="5">congue nisi. Nam pretium elementum.</tspan></text>
    <text x="60" y="209"><tspan x="60" style="font-weight:700;font-size:5px">Duis porttitor, orci sit amet</tspan><tspan x="60" dy="5">Phasellus bibendum consequat facilisis.</tspan><tspan x="60" dy="5">Vivamus non eros at enim bibendum</tspan><tspan x="60" dy="5">congue nisi. Nam pretium elementum.</tspan></text>
    <text x="88" y="250"><tspan x="88" style="font-weight:700;font-size:5px">Duis porttitor, orci sit amet</tspan><tspan x="88" dy="5">Phasellus bibendum consequat facilisis.</tspan><tspan x="88" dy="5">Vivamus non eros at enim bibendum</tspan><tspan x="88" dy="5">congue nisi. Nam pretium elementum.</tspan></text>
  </g>
  <rect x="113" y="282" width="87" height="11" fill="var(--blue)"/>
  <text x="156" y="290" class="tiny fill-white" text-anchor="middle" style="font-size:5.5px;font-weight:700">Orci varius natoque</text>
  <text x="273" y="94" class="title fill-white">ALIQUAM PRE</text>
  <text x="273" y="123" class="title"><tspan class="fill-light">CONSEQUAT</tspan><tspan class="fill-white"> ALIQUAM</tspan></text>
  <text x="275" y="150" class="body fill-white">
    <tspan x="275">Curabitur digni lorem tellus</tspan><tspan x="275" dy="12">nec euismod mollis dapibus,</tspan><tspan x="275" dy="12">ex sapien lacinia ligula, nec</tspan><tspan x="275" dy="12">ullamcorper arcu lorem vel</tspan><tspan x="275" dy="12">lorem. Sed id ante at quam.</tspan><tspan x="275" dy="12">nec ullamcorper arcu lorem</tspan><tspan x="275" dy="12">vel lorem. Sed id ante at am</tspan><tspan x="275" dy="12">euismod euismod mollis</tspan><tspan x="275" dy="12">dapibus, ex sapien lorem.</tspan>
  </text>
  <text x="422" y="150" class="body fill-white">
    <tspan x="422">Sed id ante at quam. nec</tspan><tspan x="422" dy="12">ullamcorper arcu lorem</tspan><tspan x="422" dy="12">vel lorem. Sed id ante at am</tspan><tspan x="422" dy="12">euismod euismod mollis</tspan><tspan x="422" dy="12">dapibus, ex sapien lorem.</tspan><tspan x="422" dy="12">Curabitur digni lorem tellus</tspan><tspan x="422" dy="12">nec euismod mollis dapibus,</tspan><tspan x="422" dy="12">ex sapien lacinia ligula, nec</tspan><tspan x="422" dy="12">ullamcorper arcu tellus.</tspan>
  </text>
  <text x="279" y="270" class="body-b fill-white"><tspan x="279">Duis mollis ante imperdiet Morbi molestie odio vel.</tspan><tspan x="279" dy="12">Curabitur dignissim, tellus nec euismod  mollis dapibus, ex.</tspan></text>
</svg>
</div>

<!-- Three-card slide -->
<div class="slide r2 c3">
<svg viewBox="0 0 610 342">
  <defs>
    <linearGradient id="towers" x1="0" y1="0" x2="1" y2="1">
      <stop offset="0" stop-color="#cfd2d7"/><stop offset=".5" stop-color="#eceef0"/><stop offset="1" stop-color="#b9bdc4"/>
    </linearGradient>
  </defs>
  <rect width="610" height="342" fill="url(#towers)" role="img" aria-label="Black and white photograph of glass office towers"/>
  <text x="295" y="60" class="title fill-ink" text-anchor="middle">DONEC AC SUSCIPIT MAGNA.</text>
  <g fill="var(--blue)"><rect x="48" y="82" width="157" height="200"/><rect x="226" y="82" width="157" height="200"/><rect x="405" y="82" width="157" height="200"/></g>
  <g stroke="var(--blue-light)" stroke-width="1"><line x1="64" y1="148" x2="190" y2="148"/><line x1="242" y1="148" x2="368" y2="148"/><line x1="421" y1="148" x2="547" y2="148"/></g>
  <g class="lead fill-white" style="font-size:12.5px">
    <text x="64" y="112"><tspan x="64">Suspendisse</tspan><tspan x="64" dy="16">sapien turpis.</tspan></text>
    <text x="242" y="112"><tspan x="242">Proin accumsan</tspan><tspan x="242" dy="16">posuere justo.</tspan></text>
    <text x="421" y="112"><tspan x="421">Mauris in accum</tspan><tspan x="421" dy="16">san ipsum.</tspan></text>
  </g>
  <g class="body fill-white">
    <text x="64" y="168"><tspan x="64">Euismod mollis</tspan><tspan x="64" dy="12">bus, ex sapien lacinia</tspan><tspan x="64" dy="12">ligula, nec ullamcorper</tspan><tspan x="64" dy="12">arcu lorem vel lorem.</tspan><tspan x="64" dy="12">Sed id ante at quam</tspan><tspan x="64" dy="12">euismod commodo</tspan></text>
    <text x="242" y="168"><tspan x="242">Curabitur digni</tspan><tspan x="242" dy="12">tellus nec euismod</tspan><tspan x="242" dy="12">mollis dapibus, ex</tspan><tspan x="242" dy="12">sapien lacinia ligula,</tspan><tspan x="242" dy="12">nec ullamcorper arcu</tspan><tspan x="242" dy="12">lorem vel lorem.</tspan></text>
    <text x="421" y="168"><tspan x="421">Sed id ante at</tspan><tspan x="421" dy="12">euismod commodo</tspan><tspan x="421" dy="12">quis vitae nisl ullam</tspan><tspan x="421" dy="12">corper arcu lorem.</tspan><tspan x="421" dy="12">Curabitur dignissim,</tspan><tspan x="421" dy="12">tellus nec euismod</tspan></text>
  </g>
  <g class="body-b fill-white">
    <text x="64" y="253"><tspan x="64">Duis mollis ante imperdiet</tspan><tspan x="64" dy="12">Curabitur dignissim.</tspan></text>
    <text x="242" y="253"><tspan x="242">Quisque quis dictum lacus.</tspan><tspan x="242" dy="12">Quisque efficitur.</tspan></text>
    <text x="421" y="253"><tspan x="421">Proin accumsan posuere</tspan><tspan x="421" dy="12">justo, quis tempus.</tspan></text>
  </g>
</svg>
</div>

<!-- List slide -->
<div class="slide r2 c4">
<svg viewBox="0 0 610 342">
  <rect width="610" height="342" fill="var(--white)"/>
  <polygon points="0,0 265,0 430,342 0,342" fill="var(--ink)"/>
  <polygon points="400,165 575,125 540,320" fill="url(#photo)" role="img" aria-label="Photograph of a hand using a trading tablet"/>
  <path class="stripe" d="M290 -5 L455 312" stroke="var(--blue-bright)" stroke-width="13"/>
  <path class="stripe" d="M455 312 L570 125" stroke="var(--charcoal)" stroke-width="12"/>
  <text x="372" y="95" class="title"><tspan class="fill-ink">QUISQUE </tspan><tspan class="fill-blue">VITAE</tspan></text>
  <text x="378" y="124" class="title"><tspan class="fill-blue">NIBH </tspan><tspan class="fill-ink">RUTRUM</tspan></text>
  <g>
    <g fill="var(--blue)"><rect x="58" y="92" width="80" height="19"/><rect x="58" y="140" width="80" height="19"/><rect x="58" y="190" width="80" height="19"/><rect x="58" y="242" width="80" height="19"/></g>
    <g fill="var(--white)"><polygon points="58,86 70,92 58,98"/><polygon points="58,134 70,140 58,146"/><polygon points="58,184 70,190 58,196"/><polygon points="58,236 70,242 58,248"/></g>
    <g class="tag fill-white" style="font-style:italic"><text x="76" y="105">Nam vulput</text><text x="76" y="153">Duis porttitor</text><text x="76" y="203">Pellentesque</text><text x="76" y="255">Suspendisse</text></g>
    <g fill="var(--white)"><rect x="138" y="90" width="188" height="40"/><rect x="138" y="138" width="188" height="42"/><rect x="138" y="188" width="188" height="44"/><rect x="138" y="240" width="188" height="42"/></g>
    <g fill="var(--ink)"><rect x="138" y="130" width="188" height="2"/><rect x="138" y="180" width="188" height="2"/><rect x="138" y="232" width="188" height="2"/></g>
    <g class="tiny fill-ink">
      <text x="145" y="102"><tspan style="font-size:6px;font-style:italic;font-weight:600">Aliquam a justo nisi. Cras ultricies nisi quis.</tspan><tspan x="145" dy="7">Cras pretium ipsum in enim pretium, vitae sollicitudin justo vehicula.</tspan><tspan x="145" dy="5">Curabitur accumsan vitae turpis eu placerat. Nulla pharetra blandit.</tspan><tspan x="145" dy="5">Duis velit tellus, venenatis id justo nec, auctor congue erat.</tspan></text>
      <text x="145" y="150"><tspan style="font-size:6px;font-style:italic;font-weight:600">Duis diam dolor, lacinia non nibh ut, euismod.</tspan><tspan x="145" dy="7">Cras pretium ipsum in enim pretium, vitae sollicitudin justo vehicula.</tspan><tspan x="145" dy="5">Curabitur accumsan vitae turpis eu placerat. Nulla pharetra blandit.</tspan><tspan x="145" dy="5">Duis velit tellus, venenatis id justo nec, auctor congue erat.</tspan></text>
      <text x="145" y="200"><tspan style="font-size:6px;font-style:italic;font-weight:600">Sed ornare urna eu libero auctor, a euismod.</tspan><tspan x="145" dy="7">Cras pretium ipsum in enim pretium, vitae sollicitudin justo vehicula.</tspan><tspan x="145" dy="5">Curabitur accumsan vitae turpis eu placerat. Nulla pharetra blandit.</tspan><tspan x="145" dy="5">Duis velit tellus, venenatis id justo nec, auctor congue erat.</tspan></text>
      <text x="145" y="252"><tspan style="font-size:6px;font-style:italic;font-weight:600">Vestibulum ante ipsum primis in faucibus.</tspan><tspan x="145" dy="7">Cras pretium ipsum in enim pretium, vitae sollicitudin justo vehicula.</tspan><tspan x="145" dy="5">Curabitur accumsan vitae turpis eu placerat. Nulla pharetra blandit.</tspan><tspan x="145" dy="5">Duis velit tellus, venenatis id justo nec, auctor congue erat.</tspan></text>
    </g>
  </g>
</svg>
</div>

<!-- Locations slide -->
<div class="slide r3 c1">
<svg viewBox="0 0 610 342">
  <rect width="610" height="342" fill="var(--blue)"/>
  <polygon points="0,70 165,170 0,290" fill="url(#photo)" role="img" aria-label="Photograph of a trading tablet"/>
  <path class="stripe" d="M0 58 L160 170" stroke="var(--blue-bright)" stroke-width="12"/>
  <path class="stripe" d="M160 180 L40 280" stroke="var(--white)" stroke-width="10"/>
  <text x="352" y="72" class="title fill-white" text-anchor="middle">VIVAMUS ID PURUS IPSUM</text>
  <rect x="190" y="92" width="330" height="200" rx="30" fill="#e9eefa" role="img" aria-label="World map showing office locations"/>
  <g fill="var(--blue)" stroke="var(--white)" stroke-width="2">
    <circle cx="244" cy="150" r="16"/><circle cx="364" cy="116" r="16"/><circle cx="462" cy="165" r="16"/>
    <circle cx="284" cy="210" r="16"/><circle cx="372" cy="214" r="16"/><circle cx="524" cy="248" r="16"/>
  </g>
  <g class="tiny fill-white" text-anchor="middle" style="font-size:6.5px;font-weight:600">
    <text x="244" y="149"><tspan x="244">Orci</tspan><tspan x="244" dy="7">varius</tspan></text>
    <text x="364" y="115"><tspan x="364">Cras</tspan><tspan x="364" dy="7">preti</tspan></text>
    <text x="462" y="164"><tspan x="462">Pena</tspan><tspan x="462" dy="7">Tibus</tspan></text>
    <text x="284" y="209"><tspan x="284">Ali</tspan><tspan x="284" dy="7">Quam</tspan></text>
    <text x="372" y="213"><tspan x="372">Lectus</tspan><tspan x="372" dy="7">sodal</tspan></text>
    <text x="524" y="247"><tspan x="524">Justo</tspan><tspan x="524" dy="7">Nisi</tspan></text>
  </g>
</svg>
</div>

<!-- Bar chart slide -->
<div class="slide r3 c2">
<svg viewBox="0 0 610 342">
  <rect width="610" height="342" fill="var(--white)"/>
  <polygon points="360,0 580,0 470,190" fill="var(--blue)"/>
  <polygon points="515,75 610,40 610,342 560,230" fill="url(#photo)" role="img" aria-label="Photograph of market data figures"/>
  <path class="stripe" d="M340 5 L470 240" stroke="var(--blue-bright)" stroke-width="13"/>
  <path class="stripe" d="M370 95 L425 200" stroke="var(--charcoal)" stroke-width="12"/>
  <path class="stripe" d="M470 240 L600 40" stroke="var(--blue-bright)" stroke-width="12"/>
  <text x="468" y="38" class="body-b fill-white" text-anchor="middle" style="font-size:13px"><tspan x="468">Quisque</tspan><tspan x="468" dy="16">effici</tspan><tspan x="468" dy="16">hendre</tspan></text>
  <text x="64" y="78" class="title fill-blue">SUSPENDISSE</text>
  <text x="64" y="107" class="title"><tspan class="fill-blue">SAPIEN </tspan><tspan class="fill-ink">TURPIS.</tspan></text>
  <line x1="65" y1="130" x2="65" y2="286" stroke="#c3c6cc" stroke-width="1"/>
  <line x1="65" y1="286" x2="352" y2="286" stroke="#c3c6cc" stroke-width="1"/>
  <g>
    <rect x="90" y="145" width="7" height="141" fill="var(--blue-pale)"/><rect x="101" y="163" width="7" height="123" fill="var(--blue-bright)"/><rect x="112" y="152" width="7" height="134" fill="var(--charcoal)"/>
    <rect x="141" y="183" width="7" height="103" fill="var(--blue-pale)"/><rect x="152" y="192" width="7" height="94" fill="var(--blue-bright)"/><rect x="163" y="177" width="7" height="109" fill="var(--charcoal)"/>
    <rect x="191" y="139" width="7" height="147" fill="var(--blue-pale)"/><rect x="202" y="160" width="7" height="126" fill="var(--blue-bright)"/><rect x="213" y="148" width="7" height="138" fill="var(--charcoal)"/>
    <rect x="242" y="160" width="7" height="126" fill="var(--blue-pale)"/><rect x="253" y="172" width="7" height="114" fill="var(--blue-bright)"/><rect x="264" y="152" width="7" height="134" fill="var(--charcoal)"/>
    <rect x="292" y="135" width="7" height="151" fill="var(--blue-pale)"/><rect x="303" y="143" width="7" height="143" fill="var(--blue-bright)"/><rect x="314" y="125" width="7" height="161" fill="var(--charcoal)"/>
  </g>
  <g class="label fill-blue" text-anchor="middle" style="font-size:12px"><text x="107" y="310">2019</text><text x="158" y="310">2020</text><text x="207" y="310">2021</text><text x="259" y="310">2022</text><text x="310" y="310">2023</text></g>
  <g><rect x="390" y="266" width="6" height="6" fill="var(--blue-pale)"/><rect x="390" y="283" width="6" height="6" fill="var(--blue-bright)"/><rect x="390" y="300" width="6" height="6" fill="var(--charcoal)"/></g>
  <g class="tiny fill-ink" style="font-size:6.5px"><text x="410" y="272">Quisque dictum non nulla</text><text x="410" y="289">Phasellus sit amet nec ligula</text><text x="410" y="306">Cras pulvinar tellus semper</text></g>
</svg>
</div>

<!-- Donut slide -->
<div class="slide r3 c3">
<svg viewBox="0 0 610 342">
  <rect width="610" height="342" fill="var(--ink)"/>
  <path class="stripe" d="M470 342 L510 275 L560 342" stroke="var(--blue-bright)" stroke-width="13"/>
  <path class="stripe" d="M515 280 L550 342" stroke="#d5d8de" stroke-width="10"/>
  <polygon points="455,342 490,290 525,342" fill="var(--blue)"/>
  <g transform="rotate(-90 142 148)" fill="none" stroke-width="24">
    <circle cx="142" cy="148" r="70" stroke="var(--blue)" stroke-dasharray="97 343"/>
    <circle cx="142" cy="148" r="70" stroke="var(--charcoal)" stroke-dasharray="88 352" stroke-dashoffset="-97"/>
    <circle cx="142" cy="148" r="70" stroke="var(--blue-pale)" stroke-dasharray="132 308" stroke-dashoffset="-185"/>
    <circle cx="142" cy="148" r="70" stroke="#7f9bd6" stroke-dasharray="123 317" stroke-dashoffset="-317"/>
  </g>
  <circle cx="142" cy="148" r="58" fill="var(--white)"/>
  <text x="142" y="133" class="body-b fill-ink" text-anchor="middle" style="font-size:11.5px"><tspan x="142">Bibendum</tspan><tspan x="142" dy="13">turpis vitae</tspan><tspan x="142" dy="13">malesua.</tspan></text>
  <g><rect x="64" y="234" width="7" height="7" fill="var(--blue)"/><rect x="64" y="249" width="7" height="7" fill="#7f9bd6"/><rect x="64" y="264" width="7" height="7" fill="var(--charcoal)" stroke="#666" stroke-width=".5"/><rect x="64" y="279" width="7" height="7" fill="var(--white)"/></g>
  <g class="tiny fill-white" style="font-size:7px;font-weight:600"><text x="84" y="241">Quisque dictum non nulla</text><text x="84" y="256">Phasellus sit amet nec ligula</text><text x="84" y="271">Cras pulvinar tellus semper</text><text x="84" y="286">Vivamus enim orci,</text></g>
  <text x="253" y="74" class="title"><tspan class="fill-white">PELLENT </tspan><tspan class="fill-bright">ESQUE</tspan><tspan class="fill-white"> MAGNA</tspan></text>
  <text x="253" y="98" class="body fill-white">
    <tspan x="253">Curabitur digni lorem tellus</tspan><tspan x="253" dy="12">nec euismod mollis dapibus,</tspan><tspan x="253" dy="12">ex sapien lacinia ligula, nec</tspan><tspan x="253" dy="12">ullamcorper arcu lorem vel</tspan><tspan x="253" dy="12">lorem. Sed id ante at quam.</tspan><tspan x="253" dy="12">nec ullamcorper arcu lorem</tspan><tspan x="253" dy="12">vel lorem. Sed id ante at am</tspan><tspan x="253" dy="12">euismod euismod mollis</tspan><tspan x="253" dy="12">dapibus, ex sapien lorem.</tspan>
  </text>
  <text x="400" y="98" class="body fill-white">
    <tspan x="400">Sed id ante at quam. nec</tspan><tspan x="400" dy="12">ullamcorper arcu lorem</tspan><tspan x="400" dy="12">vel lorem. Sed id ante at am</tspan><tspan x="400" dy="12">euismod euismod mollis</tspan><tspan x="400" dy="12">dapibus, ex sapien lorem.</tspan><tspan x="400" dy="12">Curabitur digni lorem tellus</tspan><tspan x="400" dy="12">nec euismod mollis dapibus,</tspan><tspan x="400" dy="12">ex sapien lacinia ligula, nec</tspan><tspan x="400" dy="12">ullamcorper arcu tellus.</tspan>
  </text>
  <text x="253" y="234" class="title-sm"><tspan x="253" class="fill-white">Porttitor</tspan><tspan x="253" dy="22" class="fill-bright">turpis sapien</tspan><tspan x="253" dy="22" class="fill-white">Suspendisse</tspan></text>
  <text x="400" y="228" class="body-b fill-white"><tspan x="400">Duis mollis ante imperdiet</tspan><tspan x="400" dy="12">Morbi molestie odio vel.</tspan></text>
</svg>
</div>

<!-- Closing slide -->
<div class="slide r3 c4">
<svg viewBox="0 0 610 342">
  <rect width="610" height="342" fill="var(--white)"/>
  <polygon points="0,0 218,0 0,330" fill="var(--blue)"/>
  <polygon points="540,0 610,0 610,342 395,342 500,120" fill="var(--ink)"/>
  <polygon points="330,260 440,120 470,342 360,342" fill="url(#photo)" role="img" aria-label="Photograph of a hand at a laptop"/>
  <path class="stripe" d="M400 342 L495 190 L580 342" stroke="var(--blue-bright)" stroke-width="13"/>
  <path class="stripe" d="M470 200 L430 280" stroke="#d5d8de" stroke-width="10"/>
  <polygon points="445,342 510,245 610,342" fill="var(--blue)"/>
  <text x="512" y="310" class="title fill-white" text-anchor="middle" style="font-size:26px">2042</text>
  <text x="512" y="322" class="tiny fill-white" text-anchor="middle" style="font-size:5.5px;font-weight:700">CURABITUR IMPERDIET</text>
  <rect x="58" y="53" width="196" height="144" rx="8" fill="var(--white)" stroke="var(--charcoal)" stroke-width="7"/>
  <rect x="148" y="200" width="16" height="10" fill="var(--charcoal)"/>
  <text x="74" y="90" class="title fill-ink" style="font-size:19px">SUSPENDISSE</text>
  <text x="74" y="116" class="title fill-blue" style="font-size:19px">SAPIEN TURPIS.</text>
  <text x="74" y="142" class="body fill-ink"><tspan x="74">Cras eget est faucibus, dapibus mi</tspan><tspan x="74" dy="12">tempor nulla. Aliquam et lobortis</tspan><tspan x="74" dy="12">Cras urna velit, dictum posuere</tspan><tspan x="74" dy="12">facilisis maximus nunc.</tspan></text>
  <text x="62" y="256" class="body fill-ink"><tspan x="62">Curabitur dignissim, tellus nec euismod</tspan><tspan x="62" dy="12">mollis dapibus, ex sapien lacinia ligula,</tspan><tspan x="62" dy="12">nec ullamcorper arcu lorem vel lorem.</tspan><tspan x="62" dy="12">Sed id ante at quam euismod commodo</tspan><tspan x="62" dy="12">quis vitae nisl ullamcorper arcu lorem.</tspan></text>
  <text x="283" y="86" class="title-sm"><tspan x="283" class="fill-ink">Porttitor</tspan><tspan x="283" dy="22" class="fill-blue">turpis sapien</tspan><tspan x="283" dy="22" class="fill-ink">Suspendisse</tspan></text>
  <text x="283" y="156" class="body-b fill-ink"><tspan x="283">Duis mollis ante imperdiet</tspan><tspan x="283" dy="12">Morbi molestie odio vel.</tspan></text>
</svg>
</div>

</body>
</html>
```